Web Page for marketing online agency

We are an online marketing agency that is acing the direct response model. We engage with our customers throughout different marketing techniques as research copy-writing, advertisements and content writing. We would need a website design that will have four main aspects: The Vision; stating who we are, The Mission; stating what we do, The Team And It's Values, and a Contact Form. For this design we would want a sharp, clean and smart approach, with illustrated elements or suggestive images. You can use the attached copy, the logo, the USP and the motto. Please integrate them as you see fit while keeping in mind the previous needs and copy. This website is going to be our connection with our possible partners, future colleagues and even our clients. You may submit a design for one page or integrate the 4 different aspects on separate web pages.
Target Market(s)
business partners, future employees, age range 25-60
Industry/Entity Type
Direct Marketing
Number of Pages Required
1 page
Requirements
Must have
- Menu / Header
- 4 Parts or 4 Pages including: vision, mission, team, contact
- Logo
- Motto: Direct Brilliance
- USP: We help people help themselves.
- The copy attached
Nice to have
- Representative illustrated images or elements
Should not have
- A boring design, classical design - WordPress like

```html
<!DOCTYPE html>
<html lang="en">
<head>
<meta charset="utf-8">
<title>NovaReach — Direct Brilliance</title>
<link rel="stylesheet" href="https://fonts.googleapis.com/css2?family=Roboto:wght@300;400;500;700;900&family=Open+Sans:wght@400;600&display=swap">
<style>
:root{
  --blue:#2d9ad9;
  --blue-dark:#1f7fbd;
  --ink:#222428;
  --text:#555a60;
  --muted:#9aa0a6;
  --line:#d9dde1;
  --grey-band:#e4e5e6;
  --dark:#2b2c2e;
  --darker:#1f2022;
  --white:#ffffff;
}
*{box-sizing:border-box;margin:0;padding:0}
html,body{width:1200px;height:2904px;overflow:hidden;background:var(--white)}
body{font-family:"Open Sans",Arial,sans-serif;color:var(--text);position:relative}
.abs{position:absolute}
h2,.nav,.btn,.band-title,.contact-title{font-family:"Roboto",Arial,sans-serif}

/* header */
.header{left:0;top:0;width:1200px;height:44px;background:var(--white);z-index:2}
.brand{left:44px;top:6px;display:flex;align-items:center;gap:8px;font-family:"Roboto",sans-serif;font-weight:700;font-size:24px;color:var(--ink)}
.brand-dot{width:14px;height:14px;border-radius:50%;background:var(--blue)}
.nav{right:150px;top:16px;display:flex;gap:30px;font-size:11px;font-weight:500;letter-spacing:.5px;color:var(--ink)}
.hero{left:0;top:44px;width:1200px;height:556px;background:linear-gradient(135deg,#d9d3c8 0%,#b8aa98 35%,#6f6a66 70%,#3d3b3c 100%)}

/* sections */
h2{font-size:30px;font-weight:900;color:var(--ink);line-height:1;letter-spacing:.3px}
.sub{font-size:13px;color:var(--muted);margin-top:4px}
.rule{width:100%;height:1px;background:var(--line);margin:12px 0 14px}
p{font-size:11.5px;line-height:1.65}
p strong{color:var(--ink)}
.btn{display:inline-block;border:1.5px solid var(--ink);padding:5px 12px;font-size:10px;font-weight:700;color:var(--ink);margin-top:16px;letter-spacing:.4px}
.btn::after{content:" ›"}
.photo{background:linear-gradient(135deg,#cfd6dc,#8a96a2)}
.photo.frame{border:6px solid var(--white);box-shadow:0 0 0 1px var(--line)}
ul.list{list-style:none;font-size:11.5px;line-height:1.9}
ul.list li::before{content:"";display:inline-block;width:5px;height:5px;background:var(--blue);border-radius:50%;margin-right:8px;vertical-align:middle}

/* values band */
.values{left:0;top:1432px;width:1200px;height:328px;background:linear-gradient(180deg,#3aa6e3,var(--blue))}
.band-title{width:100%;text-align:center;top:54px;font-size:34px;font-weight:900;color:var(--white);letter-spacing:1px}
.band-rule{left:540px;top:100px;width:120px;height:2px;background:rgba(255,255,255,.7)}
.value{top:140px;width:120px;text-align:center;color:var(--white);font-family:"Roboto",sans-serif;font-weight:700;font-size:16px}
.value svg{display:block;margin:0 auto 10px}

/* team */
.member-name{font-family:"Roboto",sans-serif;font-weight:700;font-size:14px;color:var(--ink)}
.member-role{font-size:10px;color:var(--muted);margin-bottom:8px}

/* testimonials */
.testi{left:0;top:2212px;width:1200px;height:268px;background:var(--grey-band)}
.testi h2{font-weight:700;font-size:34px}
.testi p{font-style:italic;font-size:12px}

/* contact */
.contact{left:0;top:2480px;width:1200px;height:368px;background:var(--dark)}
.contact-icon{left:576px;top:20px;width:48px;height:48px;border-radius:50%;background:var(--blue);display:flex;align-items:center;justify-content:center}
.contact-title{width:100%;text-align:center;top:84px;font-size:28px;font-weight:700;color:var(--white)}
.contact-rule{left:560px;top:122px;width:80px;height:2px;background:var(--blue)}
.field{height:30px;background:#3a3b3e;border:1px solid #4a4b4e;color:#9a9ca0;font-size:10px;padding:8px 12px}
.send{left:544px;top:308px;width:112px;height:34px;background:var(--blue);color:var(--white);font-family:"Roboto",sans-serif;font-weight:700;font-size:15px;display:flex;align-items:center;justify-content:center}
.footer{left:0;top:2848px;width:1200px;height:56px;background:var(--darker)}
.copy{left:172px;top:20px;font-size:10px;color:#8a8c90}
.socials{right:168px;top:18px;display:flex;gap:6px}
.socials span{width:20px;height:20px;background:var(--blue)}
</style>
</head>
<body>

<header class="abs header">
  <div class="abs brand"><span class="brand-dot"></span>NovaReach</div>
  <nav class="abs nav"><span>HOME</span><span>VISION</span><span>MISSION</span><span>TEAM</span><span>CONTACT</span></nav>
</header>
<div class="abs hero" role="img" aria-label="Top view of a team meeting around a desk with laptops and a handshake"></div>

<!-- vision -->
<section class="abs" style="left:172px;top:664px;width:520px">
  <h2>WHO WE ARE</h2>
  <div class="sub">Our vision</div>
  <div class="rule"></div>
  <p><strong>We are a direct response company that creates and sells information products and services that millions of people find fascinating and important in their lives.</strong></p>
  <p style="margin-top:8px">We are specialized in the self-reliance market and we serve several niche audiences. We are in the business of giving people real tools to improve their everyday choices, their health, their safety, comfort and peace of mind. We deliver them through campaigns that combine strong research, clear copy and honest offers that respect our readers and partners.</p>
  <span class="btn">READ MORE</span>
</section>
<div class="abs photo" style="left:736px;top:668px;width:134px;height:124px" role="img" aria-label="Colleagues talking at a desk"></div>
<div class="abs photo" style="left:884px;top:708px;width:144px;height:130px" role="img" aria-label="Team discussing around a laptop"></div>
<div class="abs photo" style="left:736px;top:806px;width:134px;height:120px" role="img" aria-label="Two people reviewing documents"></div>

<!-- mission -->
<div class="abs photo frame" style="left:172px;top:1008px;width:358px;height:366px" role="img" aria-label="Smiling bearded man in a checked shirt"></div>
<section class="abs" style="left:564px;top:1004px;width:470px">
  <h2>WHAT IS IT THAT WE DO</h2>
  <div class="sub">Our mission</div>
  <div class="rule"></div>
  <p><strong>We love and breathe direct response marketing.</strong></p>
  <p style="margin:6px 0">We are masters of direct response marketing, our expertise is three-fold:</p>
  <ul class="list">
    <li>We create and aggregate great information products</li>
    <li>We test and market these products to people in need</li>
    <li>We use data research to refine creative and delivery across all our channels</li>
  </ul>
  <p style="margin-top:8px">We create content that turns everyday problems into clear, helpful solutions.</p>
  <span class="btn">READ MORE</span>
</section>

<!-- values -->
<section class="abs values">
  <div class="abs band-title">VALUES</div>
  <div class="abs band-rule"></div>
  <div class="abs value" style="left:180px">
    <svg width="60" height="60" viewBox="0 0 60 60" fill="none" stroke="#fff" stroke-width="2"><circle cx="30" cy="30" r="28"/><path d="M30 16v28M20 44h20M18 22h24M18 22l-5 10h10zM42 22l-5 10h10z"/></svg>Fairness</div>
  <div class="abs value" style="left:360px">
    <svg width="60" height="60" viewBox="0 0 60 60" fill="none" stroke="#fff" stroke-width="2"><circle cx="30" cy="30" r="28"/><path d="M30 42s-12-7-12-15a6 6 0 0 1 12-2 6 6 0 0 1 12 2c0 8-12 15-12 15z"/></svg>Caring</div>
  <div class="abs value" style="left:540px">
    <svg width="60" height="60" viewBox="0 0 60 60" fill="none" stroke="#fff" stroke-width="2"><circle cx="30" cy="30" r="28"/><path d="M30 15l12 5v9c0 8-6 13-12 16-6-3-12-8-12-16v-9z"/><path d="M24 30l4 4 8-8"/></svg>Safety</div>
  <div class="abs value" style="left:720px">
    <svg width="60" height="60" viewBox="0 0 60 60" fill="none" stroke="#fff" stroke-width="2"><circle cx="30" cy="30" r="28"/><path d="M18 38l24-16M34 22h8v8M18 22l8 8"/></svg>Freedom</div>
  <div class="abs value" style="left:900px">
    <svg width="60" height="60" viewBox="0 0 60 60" fill="none" stroke="#fff" stroke-width="2"><circle cx="30" cy="30" r="28"/><path d="M24 24a6 6 0 1 1 8 6c-2 1-2 3-2 5"/><circle cx="30" cy="41" r="1.5" fill="#fff"/></svg>Help</div>
</section>

<!-- team -->
<section class="abs" style="left:172px;top:1820px;width:860px">
  <h2>OUR TEAM &amp; VALUES</h2>
  <div class="sub">Our vision</div>
</section>
<div class="abs photo" style="left:172px;top:1884px;width:128px;height:112px" role="img" aria-label="Portrait of a team member"></div>
<div class="abs" style="left:328px;top:1884px;width:700px">
  <div class="member-name">Liam Carter</div>
  <div class="member-role">CEO &amp; Founder</div>
  <p>I have worked in direct response for over ten years, building campaigns that help people find what they need. Our team shares one belief: when we help people help themselves, everyone wins.</p>
  <span class="btn">READ MORE</span>
</div>
<div class="abs photo" style="left:888px;top:2024px;width:144px;height:132px" role="img" aria-label="Portrait of a team member in a suit"></div>
<div class="abs" style="left:172px;top:2024px;width:690px;text-align:right">
  <div class="member-name">Adam Reeves</div>
  <div class="member-role">Head of Research &amp; Copy</div>
  <p>Since the company was founded, I have led our research and copy teams, turning careful study of our readers into clear, honest offers that perform across every channel we use.</p>
  <span class="btn">READ MORE</span>
</div>

<!-- testimonials -->
<section class="abs testi">
  <svg class="abs" style="left:164px;top:70px" width="116" height="96" viewBox="0 0 116 96" fill="#333">
    <path d="M0 48C0 20 14 4 40 0l4 10C28 16 22 26 22 38h26v58H0zM64 48C64 20 78 4 104 0l4 10C92 16 86 26 86 38h26v58H64z"/>
  </svg>
  <div class="abs" style="left:400px;top:56px;width:640px">
    <h2>Testimonials</h2>
    <div class="rule" style="width:220px;background:#bbb"></div>
    <p>“Working with this team changed the way we think about our customers. Every campaign is built on solid research and clear, honest copy, and the results speak for themselves. They are true partners who care about the long-term growth of every client they serve.” — Daniel Moore</p>
  </div>
</section>

<!-- contact -->
<section class="abs contact">
  <div class="abs contact-icon">
    <svg width="22" height="16" viewBox="0 0 22 16" fill="none" stroke="#fff" stroke-width="2"><rect x="1" y="1" width="20" height="14"/><path d="M1 1l10 8 10-8"/></svg>
  </div>
  <div class="abs contact-title">CONTACT FORM</div>
  <div class="abs contact-rule"></div>
  <div class="abs field" style="left:172px;top:148px;width:276px">Enter your name</div>
  <div class="abs field" style="left:462px;top:148px;width:276px">Enter your email</div>
  <div class="abs field" style="left:752px;top:148px;width:280px">Enter your phone</div>
  <div class="abs field" style="left:172px;top:192px;width:860px;height:92px">Enter your message</div>
  <div class="abs send">SEND</div>
</section>

<footer class="abs footer">
  <div class="abs copy">Copyright 2016 NovaReach.com All Rights Reserved</div>
  <div class="abs socials"><span></span><span></span><span></span><span></span><span></span></div>
</footer>

</body>
</html>
```